Modern Spot UV Business Card design

We are a relatively new real estate agency. We need a business card that reflects the professionalism and prestige of our company but is also modern and fresh, based around our logo.
We would love to utilise spot UV.
Happy to let the designers use their imagination and see what they come up with (we're not very creative, so have no ideas for you, sorry) :-)
We'd like one for each staff member, but I've just provided one staff members photo here to avoid confusion.

Target Market(s)

Families

Industry/Entity Type

Real Estate Agent

Contact Information for Business Card

Colin Varga - Director & Principal
Mobile: 0491 527 806
Email: colin.varga@vbrokers.example.com.au
Phone: (08) 7364 9150
Fax: (08) 7364 9182
www.vargabrokersrealestate.example.com.au

Font styles to use
Other font styles liked:
• Kabel Dm BT

Requirements
Must have
• Contact details, logo, photo, spot UV
Nice to have
• Modern interesting features that will make people comment. Nothing too feminine nor too masculine.
Should not have
• No houses! Nothing typical of a real estate agent.

```html
<!DOCTYPE html>
<html lang="en">
<head>
<meta charset="utf-8">
<title>VargaBrokers Real Estate – Business Card</title>
<link rel="stylesheet" href="https://fonts.googleapis.com/css2?family=Questrial&display=swap">
<style>
  :root {
    --stage: #3a3431;
    --card-back: #1b1c1e;
    --card-front: #26282b;
    --uv-gloss: #5b5e63;
    --white: #ffffff;
    --blue: #1f8fd6;
    --orange: #f39a1e;
    --photo-top: #2e3034;
    --photo-bottom: #6f7276;
  }
  * { margin: 0; padding: 0; box-sizing: border-box; }
  html, body { width: 1200px; height: 780px; overflow: hidden; }
  body {
    background: var(--stage);
    font-family: "Questrial", sans-serif;
    display: flex;
    align-items: center;
    justify-content: center;
    gap: 40px;
  }
  .card {
    position: relative;
    width: 550px;
    height: 314px;
    border-radius: 3px;
    overflow: hidden;
  }

  /* Brand name set as plain text with one circle */
  .brand {
    display: flex;
    align-items: center;
    gap: 10px;
    font-size: 30px;
    line-height: 1;
    white-space: nowrap;
  }
  .brand__dot {
    width: 12px;
    height: 12px;
    border-radius: 50%;
    background: currentColor;
    flex: none;
  }

  /* Back side: spot UV name */
  .card--back {
    background: var(--card-back);
    display: flex;
    align-items: center;
    justify-content: center;
  }
  .brand--uv { color: var(--uv-gloss); }

  /* Front side */
  .card--front { background: var(--card-front); color: var(--white); }
  .brand--front {
    position: absolute;
    left: 150px;
    top: 42px;
    color: var(--white);
  }
  .agent {
    position: absolute;
    left: 36px;
    top: 112px;
  }
  .agent__name {
    color: var(--blue);
    font-size: 16px;
    letter-spacing: 0.5px;
    text-transform: uppercase;
  }
  .agent__role { font-size: 15px; margin-top: 2px; }
  .contact {
    position: absolute;
    left: 36px;
    top: 168px;
    list-style: none;
    font-size: 15px;
    line-height: 19px;
  }
  .contact__item { display: flex; align-items: center; gap: 7px; }
  .contact__icon { width: 12px; height: 12px; flex: none; }
  .website {
    position: absolute;
    left: 36px;
    top: 262px;
    font-size: 15px;
    color: var(--orange);
  }
  .agent-photo {
    position: absolute;
    right: 0;
    bottom: 0;
    width: 170px;
    height: 210px;
    background: linear-gradient(180deg, var(--photo-top), var(--photo-bottom));
  }
</style>
</head>
<body>

  <section class="card card--back">
    <div class="brand brand--uv">
      <span>VargaBrokers Real Estate</span><span class="brand__dot"></span>
    </div>
  </section>

  <section class="card card--front">
    <div class="brand brand--front">
      <span>VargaBrokers Real Estate</span><span class="brand__dot"></span>
    </div>

    <div class="agent">
      <div class="agent__name">Colin Varga</div>
      <div class="agent__role">Director &amp; Principal</div>
    </div>

    <ul class="contact">
      <li class="contact__item">
        <svg class="contact__icon" viewBox="0 0 12 12"><rect x="3" y="0.5" width="6" height="11" rx="1" fill="none" stroke="var(--orange)" stroke-width="1.2"/><circle cx="6" cy="9.5" r="0.8" fill="var(--orange)"/></svg>
        <span>0491 527 806</span>
      </li>
      <li class="contact__item">
        <svg class="contact__icon" viewBox="0 0 12 12"><path d="M1 4 Q6 0 11 4 L9.5 5.5 L8 4 L4 4 L2.5 5.5 Z" fill="var(--orange)"/><rect x="2" y="6" width="8" height="5" rx="1" fill="var(--orange)"/></svg>
        <span>(08) 7364 9150</span>
      </li>
      <li class="contact__item">
        <svg class="contact__icon" viewBox="0 0 12 12"><rect x="3" y="0.5" width="6" height="4" fill="var(--orange)"/><rect x="1" y="5" width="10" height="6" rx="1" fill="var(--orange)"/></svg>
        <span>(08) 7364 9182</span>
      </li>
      <li class="contact__item">
        <svg class="contact__icon" viewBox="0 0 12 12"><rect x="0.5" y="2" width="11" height="8" fill="var(--orange)"/><path d="M0.5 2 L6 6.5 L11.5 2" fill="none" stroke="var(--card-front)" stroke-width="1"/></svg>
        <span>colin.varga@vbrokers.example.com.au</span>
      </li>
    </ul>

    <div class="website">www.vargabrokersrealestate.example.com.au</div>

    <div class="agent-photo" role="img" aria-label="Portrait photo of the agent in a grey suit and striped shirt"></div>
  </section>

</body>
</html>
```